A reimagined website for a cross-border tax firm

There are two aspects to this project for Brindlemoor Tax Advisory:
1) I need a logo update to accommodate increasing focus and specialization in my business. The byline under the name “Brindlemoor Tax Advisory” needs to change:
ORIGINAL: TAX SUPPORT FOR PUBLIC ACCOUNTING FIRMS
REVISED: CROSS-BORDER TAX SERVICES • U.S. & CANADA
2) I need a website “refresh” (see current website at www.levyhelpdesk.example) based on this logo – a new vision for a website with greater clarity, focus and organization. It should represent a re-envisioning of the current approach, and not the wholesale abandonment of the style represented there. I need it to be creative, compelling and attention grabbing, but still professional. This should, at a minimum, update any places where the old name/logo is used, but I want the redesign to go beyond this to something more intuitive. I need high quality separate PNG files of the various logo styles for use in various documents, but HTML coding would be a helpful but not necessary addition.

Target Market(s)

People in need of cross-border tax services - Canada and US

Coding

Number of Pages Required

Requirements
Must have
• Greater crispness, sharpness - higher resolution
• A more compelling, organized approach - make the wording and images more accessible to the website user (especially the staff bios, which have scroll bars now)
Nice to have
• Replacement of stock image with a true image of the Halifax skyline
Should not have
• Deviate from colour pattern represented in website logo of blue/orange
• Deviate from existing logo except for word replacement

```html
<!DOCTYPE html>
<html lang="en">
<head>
<meta charset="utf-8">
<title>Brindlemoor Tax Advisory</title>
<link href="https://fonts.googleapis.com/css2?family=Open+Sans:ital,wght@0,400;0,600;0,700;0,800;1,400&display=swap" rel="stylesheet">
<style>
:root{
  --orange:#f47a20;
  --orange-dark:#d9621a;
  --leather:#1c1c1c;
  --leather-light:#2a2a2a;
  --navy:#1b2f55;
  --navy-deep:#14233f;
  --blue:#1f6dc2;
  --tan:#e3b985;
  --white:#ffffff;
  --muted:#c9c9c9;
  --ink:#333333;
}
*{margin:0;padding:0;box-sizing:border-box}
html,body{width:1200px;height:3884px;overflow:hidden}
body{font-family:"Open Sans",Arial,sans-serif;color:var(--white);background:var(--leather);position:relative}
.abs{position:absolute}

/* header */
.site-header{left:0;top:0;width:1200px;height:248px;background:radial-gradient(ellipse at center,var(--leather-light),#111 80%)}
.brand{left:230px;top:44px;display:flex;align-items:center;gap:28px}
.brand-square{width:160px;height:160px;background:var(--blue)}
.brand-name{font-family:"Open Sans",Arial,sans-serif;font-weight:700;font-size:40px;color:var(--white);white-space:nowrap}
.brand-tagline{font-size:19px;color:var(--muted);margin-top:10px;white-space:nowrap}

/* hero */
.hero{left:0;top:248px;width:1200px;height:1142px;background:linear-gradient(180deg,#7fb3e6 0%,#b9d6f0 22%,#6a7f95 45%,#8a7b6a 62%,#4d6a86 80%,#2f4d6b 100%)}
.side-nav{left:0;top:460px;width:232px;list-style:none}
.side-nav li{height:104px;display:flex;align-items:center;padding-left:50px;font-size:22px;font-weight:600;color:#222;background:rgba(255,255,255,.78);border-bottom:1px solid rgba(0,0,0,.06)}
.side-nav li.active{background:var(--tan)}
.hero-title{left:232px;top:730px;width:968px;text-align:center;font-weight:800;font-size:78px;letter-spacing:2px;text-shadow:0 3px 8px rgba(0,0,0,.6)}
.hero-sub{left:232px;top:832px;width:968px;text-align:center;font-style:italic;font-size:42px;text-shadow:0 2px 6px rgba(0,0,0,.6)}
.cta-label{left:232px;top:1218px;width:968px;text-align:center;font-weight:700;font-size:22px;letter-spacing:1px}
.cta-form{left:430px;top:1278px;display:flex}
.cta-form .field{width:440px;height:44px;background:#fff;color:#777;font-size:18px;padding:10px 16px}
.cta-form .send{width:120px;height:44px;background:var(--orange);font-weight:700;font-size:18px;display:flex;align-items:center;justify-content:center}

/* service tiles */
.tile{top:1390px;width:596px;height:280px}
.tile .photo{width:100%;height:190px;background:linear-gradient(135deg,#e8c491,#c98e4c)}
.tile .label{height:90px;background:var(--orange);display:flex;align-items:center;justify-content:center;font-size:34px;font-weight:600}
.tile-left{left:0}
.tile-right{left:604px}
.tile-divider{left:596px;top:1390px;width:8px;height:280px;background:#fff}

/* team */
.team{left:0;top:1670px;width:1200px;height:890px;background:radial-gradient(ellipse at 50% 40%,var(--leather-light),#141414 85%)}
.section-title{width:1200px;text-align:center;font-size:44px;font-weight:600}
.team .section-title{top:90px}
.team-photo{left:120px;top:240px;width:232px;height:480px;border:3px solid var(--orange);background:linear-gradient(180deg,#8a8a8a,#3a3a44)}
.team-name{left:532px;top:234px;font-size:32px;font-weight:600}
.team-bio{left:532px;top:300px;width:500px;font-size:17px;line-height:26px;color:#ddd}
.team-bio p{margin-bottom:22px}
.team-rule{left:1068px;top:240px;width:2px;height:480px;background:var(--orange)}
.team-dot{left:1060px;top:520px;width:18px;height:18px;border-radius:50%;background:var(--orange)}
.btn-next{left:532px;top:676px;width:144px;height:42px;border-radius:21px;background:var(--orange);font-weight:700;font-size:16px;display:flex;align-items:center;justify-content:center}

/* testimonials */
.testimonials{left:0;top:2560px;width:1200px;height:560px;background:var(--orange)}
.testimonials .section-title{top:62px}
.quote-back{left:280px;top:200px;width:660px;height:180px;background:var(--orange-dark)}
.quote-card{left:320px;top:180px;width:580px;height:250px;background:#fff;color:var(--ink);text-align:center;padding:70px 60px 0}
.quote-card p{font-style:italic;font-size:17px;line-height:26px;color:#9a9a9a}
.quote-card .client{margin-top:18px;font-size:17px;color:#222}
.avatar{left:563px;top:140px;width:74px;height:74px;border-radius:50%;background:linear-gradient(180deg,#c9b19a,#6d5a4c);border:4px solid #fff}
.qmark{font-family:Georgia,serif;font-size:110px;font-weight:700;color:var(--orange);line-height:1}
.q-open{left:340px;top:140px}
.q-close{left:780px;top:335px}
.arrow{top:260px}

/* contact */
.contact{left:0;top:3120px;width:1200px;height:460px;background:var(--navy)}
.contact-card{left:175px;top:20px;width:340px;height:440px;background:var(--blue);padding:30px 28px}
.contact-card h2{font-size:26px;font-weight:700;margin-bottom:34px}
.contact-item{display:flex;align-items:center;gap:28px;height:86px;font-size:19px}
.contact-intro{left:535px;top:36px;width:500px;text-align:center;font-size:15px;line-height:23px}
.form-label{font-size:15px}
.form-line{height:2px;background:rgba(255,255,255,.7)}
.btn-send{left:888px;top:398px;width:140px;height:40px;border:2px solid #fff;border-radius:8px;font-weight:700;font-size:16px;display:flex;align-items:center;justify-content:center}

/* footer */
.site-footer{left:0;top:3580px;width:1200px;height:304px;background:var(--navy-deep)}
.footer-nav{left:0;top:22px;width:1200px;display:flex;justify-content:center;gap:44px;font-size:24px;color:var(--orange);list-style:none}
.footer-brand{left:0;top:90px;width:1200px;display:flex;justify-content:center;align-items:center;gap:18px}
.footer-brand .brand-square{width:78px;height:78px}
.footer-brand .brand-name{font-size:24px}
.footer-brand .brand-tagline{font-size:12px;margin-top:6px}
.follow{left:0;top:210px;width:1200px;text-align:center;font-size:14px;font-weight:700;letter-spacing:1px}
.socials{left:0;top:238px;width:1200px;display:flex;justify-content:center;gap:16px}
.socials span{width:36px;height:36px;border-radius:50%;background:#fff}
</style>
</head>
<body>

<header class="site-header abs">
  <div class="brand abs">
    <div class="brand-square"></div>
    <div>
      <div class="brand-name">BRINDLEMOOR TAX ADVISORY</div>
      <div class="brand-tagline">Cross-Border Tax Services • U.S. &amp; Canada</div>
    </div>
  </div>
</header>

<section class="hero abs" role="img" aria-label="Harbour skyline with tall ship and office towers under a blue sky"></section>
<ul class="side-nav abs">
  <li class="active">Home</li>
  <li>Our Team</li>
  <li>Services</li>
  <li>Testimonials</li>
  <li>Upload Files</li>
  <li>Contact</li>
  <li>Payment</li>
</ul>
<h1 class="hero-title abs">LOREM IPSUM DOLOR</h1>
<div class="hero-sub abs">sit amet, consectetur adipiscing elit.</div>
<div class="cta-label abs">CONTACT US NOW</div>
<div class="cta-form abs">
  <div class="field">Email</div>
  <div class="send">SEND</div>
</div>

<div class="tile tile-left abs">
  <div class="photo" role="img" aria-label="Hands working on tax papers with a calculator"></div>
  <div class="label">For Individuals</div>
</div>
<div class="tile-divider abs"></div>
<div class="tile tile-right abs">
  <div class="photo" role="img" aria-label="Accounting team meeting around a table"></div>
  <div class="label">For Public &nbsp;Accounting Firms</div>
</div>

<section class="team abs">
  <h2 class="section-title abs">Our Team</h2>
  <div class="team-photo abs" role="img" aria-label="Portrait of a staff member in a suit"></div>
  <h3 class="team-name abs">Dorian K. Wexley, CPA, CGA, EA</h3>
  <div class="team-bio abs">
    <p>Dorian has been practicing tax for over 17 years.</p>
    <p>Educated at Lakeshore University and Northvale University, he began his career in the Mississauga office of Carrow &amp; Finch LLP in September 1998. After a short period in the audit practice, he transferred to the tax division where he focused on Canadian corporate and US personal tax compliance (that is, the preparation and filing of tax returns).</p>
    <p>In January 2001 he took a position in the Millbrook, Nova Scotia office of Hollis Bray LLP, where he continued his work in US tax compliance.</p>
  </div>
  <div class="team-rule abs"></div>
  <div class="team-dot abs"></div>
  <div class="btn-next abs">NEXT</div>
</section>

<section class="testimonials abs">
  <h2 class="section-title abs">Testimonials</h2>
  <div class="quote-back abs"></div>
  <div class="quote-card abs">
    <p>Clear advice on both returns, delivered on time and explained plainly. Filing across the border finally felt simple and well organized for our whole family this year.</p>
    <div class="client">Client's Name</div>
  </div>
  <div class="qmark q-open abs">“</div>
  <div class="qmark q-close abs">”</div>
  <div class="avatar abs" role="img" aria-label="Client photo"></div>
  <svg class="arrow abs" style="left:212px" width="28" height="40" viewBox="0 0 28 40"><path d="M22 4 6 20l16 16" fill="none" stroke="#fff" stroke-width="5"/></svg>
  <svg class="arrow abs" style="left:960px" width="28" height="40" viewBox="0 0 28 40"><path d="M6 4l16 16L6 36" fill="none" stroke="#fff" stroke-width="5"/></svg>
</section>

<section class="contact abs">
  <div class="contact-card abs">
    <h2>CONTACT US</h2>
    <div class="contact-item">
      <svg width="26" height="34" viewBox="0 0 26 34"><path d="M13 0C6 0 0 6 0 13c0 9 13 21 13 21s13-12 13-21C26 6 20 0 13 0z" fill="var(--orange)"/><circle cx="13" cy="13" r="5" fill="var(--blue)"/></svg>
      <span>Address</span>
    </div>
    <div class="contact-item">
      <svg width="30" height="26" viewBox="0 0 30 26"><rect x="0" y="4" width="30" height="22" rx="4" fill="var(--orange)"/><rect x="6" y="0" width="18" height="8" rx="3" fill="var(--orange)"/><circle cx="15" cy="16" r="5" fill="var(--blue)"/></svg>
      <span>555 010 2748</span>
    </div>
    <div class="contact-item">
      <svg width="30" height="22" viewBox="0 0 30 22"><rect width="30" height="22" fill="var(--orange)"/><path d="M0 0l15 12L30 0" fill="none" stroke="var(--blue)" stroke-width="2"/></svg>
      <span>email address</span>
    </div>
    <div class="contact-item">
      <svg width="30" height="30" viewBox="0 0 30 30"><circle cx="15" cy="15" r="14" fill="var(--orange)"/><path d="M15 7v9h7" fill="none" stroke="var(--blue)" stroke-width="3"/></svg>
      <span>office hours</span>
    </div>
  </div>
  <p class="contact-intro abs">If you have questions, comments or would like a quotation, we would love to hear from you. Just call our office 555 010 2748, or fill out this form, and we'll gladly answer all of your questions.</p>
  <div class="form-label abs" style="left:540px;top:162px">Name</div>
  <div class="form-line abs" style="left:540px;top:200px;width:216px"></div>
  <div class="form-label abs" style="left:800px;top:162px">Email</div>
  <div class="form-line abs" style="left:800px;top:200px;width:228px"></div>
  <div class="form-label abs" style="left:540px;top:244px">Phone</div>
  <div class="form-line abs" style="left:540px;top:278px;width:216px"></div>
  <div class="form-label abs" style="left:800px;top:244px">Subject</div>
  <div class="form-line abs" style="left:800px;top:278px;width:228px"></div>
  <div class="form-label abs" style="left:540px;top:306px">Message</div>
  <div class="form-line abs" style="left:540px;top:376px;width:488px"></div>
  <div class="btn-send abs">SEND</div>
</section>

<footer class="site-footer abs">
  <ul class="footer-nav abs">
    <li>Home</li><li>Our Team</li><li>Services</li><li>Testimonials</li><li>Upload Files</li><li>Contact</li><li>Payment</li>
  </ul>
  <div class="footer-brand abs">
    <div class="brand-square"></div>
    <div>
      <div class="brand-name">BRINDLEMOOR TAX ADVISORY</div>
      <div class="brand-tagline">Cross-Border Tax Services • U.S. &amp; Canada</div>
    </div>
  </div>
  <div class="follow abs">FOLLOW US</div>
  <div class="socials abs"><span></span><span></span><span></span></div>
</footer>

</body>
</html>
```